Business Card 85x40mm - Freelance audio mixing / live event operator

I am a freelance audio operator working in live events. Mostly corporate events mixing sound for a range of entertainment, awards nights and functions. I need a new card to give to perspective clients.

The final design will convey bold professionalism with a general dark vibe. Looking for dark-ish background with some smatterings of colour added.

I have attatched my old BC for an idea of what I have liked in the past. Id like a more modern updated design (that circular design on the back is not my logo it is just a picture I found that resembled sound} . For an added element possibly a mixture of some playful colours in a way that resembles an audio wave form or sound.

I have attached a photo called "audio software" with some colourful squiggly lines; maybe incorporate elements of that into into design
Updates

Added extra $ to project Damn Pixel herds fees are unreasonable

Target Market(s)

Mostly corporate clients

Industry/Entity Type

Events

Contact Information for Business Card

Corwin Blaylock
Sound | FOH | Monitors | Systems | Corporate

Digital Audio Mixing Specialist, Live Event Technical Professional,

corwinblaylock@mailvane.net, +61 408 315 927

Colors
ec1f27
ffc214
9bcb3c
6b449b

Requirements
Must have
• Dark theme
• 85x40mm dimensions
Nice to have
• some sort of imagery or design to reflect audio/sound

```html
<!DOCTYPE html>
<html lang="en">
<head>
<meta charset="utf-8">
<title>Corwin Blaylock — Business Card</title>
<link rel="stylesheet" href="https://fonts.googleapis.com/css2?family=Arvo:wght@400;700&family=Open+Sans:wght@400&display=swap">
<style>
  :root {
    --backdrop: #2b2725;
    --card: #0d0d0d;
    --card-edge: #1a1a1a;
    --green: #9bcb3c;
    --yellow: #ffc214;
    --red: #ec1f27;
    --text: #e6e6e6;
    --silver: #c9c9c9;
  }
  * { box-sizing: border-box; margin: 0; padding: 0; }
  html, body {
    width: 1200px;
    height: 844px;
    overflow: hidden;
    background: var(--backdrop);
  }
  .stage {
    width: 1200px;
    height: 844px;
    display: flex;
    align-items: center;
    justify-content: center;
    gap: 60px;
  }
  .card {
    width: 520px;
    height: 300px;
    background: var(--card);
    border: 1px solid var(--card-edge);
    box-shadow: 0 18px 40px rgba(0,0,0,.55);
    position: relative;
  }

  /* Contact side */
  .card--contact {
    padding: 46px 0 0 96px;
    font-family: "Open Sans", Arial, sans-serif;
    color: var(--text);
  }
  .contact__name {
    font-family: "Arvo", Georgia, serif;
    font-weight: 700;
    font-size: 31px;
    line-height: 1;
    display: inline-block;
    padding-bottom: 4px;
    border-bottom: 3px solid var(--red);
  }
  .contact__name-first { color: var(--green); }
  .contact__name-last { color: var(--yellow); }
  .contact__title {
    margin-top: 14px;
    margin-left: 40px;
    font-size: 14px;
    line-height: 1.3;
  }
  .contact__rule {
    width: 210px;
    height: 1px;
    background: var(--red);
    margin: 12px 0 12px 40px;
  }
  .contact__details {
    margin-left: 72px;
    font-size: 14px;
    line-height: 1.35;
  }
  .contact__details .phone { padding-left: 28px; }
  .contact__services {
    margin-top: 20px;
    margin-left: -20px;
    font-size: 15px;
    letter-spacing: .3px;
  }

  /* Brand side */
  .card--brand {
    display: flex;
    align-items: center;
    justify-content: center;
    gap: 16px;
  }
  .brand__mark {
    width: 26px;
    height: 26px;
    border: 3px solid var(--silver);
  }
  .brand__name {
    font-family: "Arvo", Georgia, serif;
    font-weight: 700;
    font-size: 34px;
    color: var(--silver);
  }
</style>
</head>
<body>
  <main class="stage">
    <section class="card card--contact">
      <h1 class="contact__name"><span class="contact__name-first">Corwin</span> <span class="contact__name-last">Blaylock</span></h1>
      <p class="contact__title">Digital Audio Mixing Specialist,<br>Live Event Technical Professional</p>
      <div class="contact__rule"></div>
      <p class="contact__details">
        <span class="phone">+61 408 315 927</span><br>
        corwinblaylock@mailvane.net
      </p>
      <div class="contact__rule"></div>
      <p class="contact__services">Sound | FOH | Monitors | Systems | Corporate</p>
    </section>

    <section class="card card--brand">
      <span class="brand__mark"></span>
      <span class="brand__name">Corwin Blaylock</span>
    </section>
  </main>
</body>
</html>
```